Brightpath Orthodontics business card design

Need a business card design that reflects our re-branding (orthodontic office - braces) and a new partnership with a pediatric dental office. We would like to include "for adults and children" on the card as well so adults know they are welcome to get their braces here as well. Office design is modern and would like business card to reflect a modern type look. Here's the text we would like to be included on the card:

Darren Holloway, DDS, MSD
5214 West Maple Avenue, Suite 204
Linden Falls, OR 97099
817-555-0143
www.brightpathortho.example
info@brightpathortho.example
Updates

Can we add the following to the existing designs? Darren Holloway, DDS, MSD 5214 West Maple Avenue, Suite 204 Linden Falls, OR 97099 817-555-0143

Does anyone have any more vertical designs available? Thanks!

Industry/Entity Type

Dental

```html
<!DOCTYPE html>
<html lang="en">
<head>
<meta charset="utf-8">
<title>Brightpath Orthodontics – Business Card</title>
<link rel="stylesheet" href="https://fonts.googleapis.com/css2?family=Questrial&display=swap">
<style>
  :root {
    --bg: #2e2e2e;
    --card: #f7f7f7;
    --blue: #1469ad;
    --blue-line: #1a6fb3;
    --white: #ffffff;
    --ink: #1f1f1f;
    --yellow: #e8e21a;
    --magenta: #d6157e;
    --green: #86bd36;
    --orange: #e8861f;
    --black: #0c0c0c;
  }
  * { box-sizing: border-box; margin: 0; padding: 0; }
  html, body { width: 1200px; height: 1116px; overflow: hidden; }
  body {
    background: var(--bg);
    font-family: "Questrial", "Century Gothic", sans-serif;
    position: relative;
  }
  .card {
    position: absolute;
    left: 310px; top: 68px;
    width: 580px; height: 980px;
    background: var(--card);
    border-radius: 36px;
    overflow: hidden;
    box-shadow: 0 18px 40px rgba(0,0,0,.55);
  }
  .tabs {
    position: absolute; left: 0; right: 0;
    display: flex; gap: 4px; padding: 0 30px;
    height: 34px;
  }
  .tabs--top { top: 0; }
  .tabs--bottom { bottom: 0; }
  .tab { flex: 1; }
  .tabs--top .tab { border-radius: 0 0 8px 8px; }
  .tabs--bottom .tab { border-radius: 8px 8px 0 0; }
  .tab--yellow { background: var(--yellow); }
  .tab--blue { background: var(--blue); }
  .tab--magenta { background: var(--magenta); }
  .tab--green { background: var(--green); }
  .tab--orange { background: var(--orange); }
  .tab--black { background: var(--black); }

  .rule {
    position: absolute; left: 0; right: 0; height: 5px;
    background: var(--blue-line);
  }
  .band {
    position: absolute; left: 0; right: 0;
    background: var(--blue);
    color: var(--white);
  }
  .band::before, .band::after {
    content: ""; position: absolute; left: 0; right: 0;
    height: 3px; background: rgba(255,255,255,.9);
  }
  .band::before { top: 10px; }
  .band::after { bottom: 10px; }

  .band--name { top: 84px; height: 122px; text-align: center; padding-top: 28px; }
  .doctor-name { font-size: 38px; letter-spacing: 2px; line-height: 1.1; }
  .doctor-title { font-size: 20px; letter-spacing: 2px; margin-top: 2px; }

  .brand {
    position: absolute; left: 0; right: 0; top: 222px; height: 226px;
    display: flex; flex-direction: column; align-items: center; justify-content: center;
  }
  .brand-row { display: flex; align-items: center; gap: 20px; }
  .brand-dot { width: 52px; height: 52px; border-radius: 50%; background: var(--blue); flex: none; }
  .brand-name {
    font-size: 44px; line-height: 1.15; font-weight: 400;
    color: var(--ink);
  }
  .tagline {
    margin-top: 20px; font-size: 22px; letter-spacing: 1px; color: var(--ink);
  }

  .band--contact { top: 462px; height: 370px; padding: 60px 0 0 70px; }
  .contact { list-style: none; }
  .contact li {
    display: flex; align-items: center; gap: 22px;
    font-size: 25px; letter-spacing: .5px; height: 58px;
  }
  .contact li.indent { padding-left: 54px; }
  .contact svg { width: 32px; height: 32px; flex: none; fill: var(--white); }
</style>
</head>
<body>
  <div class="card">
    <div class="tabs tabs--top">
      <span class="tab tab--yellow"></span><span class="tab tab--blue"></span><span class="tab tab--magenta"></span>
      <span class="tab tab--green"></span><span class="tab tab--orange"></span><span class="tab tab--black"></span>
    </div>
    <div class="rule" style="top:64px"></div>

    <header class="band band--name">
      <div class="doctor-name">Darren Holloway</div>
      <div class="doctor-title">DDS, MSD</div>
    </header>

    <section class="brand">
      <div class="brand-row">
        <span class="brand-dot"></span>
        <div class="brand-name">Brightpath<br>Orthodontics</div>
      </div>
      <div class="tagline">For adults &amp; children</div>
    </section>

    <section class="band band--contact">
      <ul class="contact">
        <li>
          <svg viewBox="0 0 32 32"><path d="M4 12c0-4 5-6 12-6s12 2 12 6v2h-7v-3h-10v3H4zM8 16h16l3 10H5zM16 18a3.5 3.5 0 1 0 0 7 3.5 3.5 0 0 0 0-7z"/></svg>
          817-555-0143
        </li>
        <li>
          <svg viewBox="0 0 32 32"><path d="M16 3a13 13 0 1 0 0 26 13 13 0 0 0 0-26zm0 3a10 10 0 0 1 9.9 8.5h-5.5c-.3-3-1.4-5.9-3-8.4zm-3.5.6c-1.5 2.3-2.4 5-2.7 7.9H6.1a10 10 0 0 1 6.4-7.9zM6.1 17.5h3.7c.3 2.9 1.2 5.6 2.7 7.9a10 10 0 0 1-6.4-7.9zm7.7 0h4.5c-.3 2.6-1 5-2.3 7.1-1.3-2.1-2-4.5-2.2-7.1zm0-3c.2-2.6 1-5 2.2-7.1 1.3 2.1 2 4.5 2.3 7.1zm6.6 3h5.5a10 10 0 0 1-7.2 8.1c1-2.4 1.6-5.2 1.7-8.1z"/></svg>
          www.brightpathortho.example
        </li>
        <li>
          <svg viewBox="0 0 32 32"><path d="M3 7h26v18H3zm2.5 2.5L16 18l10.5-8.5z"/></svg>
          info@brightpathortho.example
        </li>
        <li>
          <svg viewBox="0 0 32 32"><path d="M16 2a9 9 0 0 0-9 9c0 7 9 19 9 19s9-12 9-19a9 9 0 0 0-9-9zm0 5.5a3.5 3.5 0 1 1 0 7 3.5 3.5 0 0 1 0-7z"/></svg>
          5214 West Maple Avenue, Suite 204
        </li>
        <li class="indent">Linden Falls, OR 97099</li>
      </ul>
    </section>

    <div class="rule" style="top:880px"></div>
    <div class="tabs tabs--bottom">
      <span class="tab tab--yellow"></span><span class="tab tab--blue"></span><span class="tab tab--magenta"></span>
      <span class="tab tab--green"></span><span class="tab tab--orange"></span><span class="tab tab--black"></span>
    </div>
  </div>
</body>
</html>
```